Website for IT consulting Company

I need a website upgrade, the existing site content is ok, I would also like to add a testimonial page, the site should be something that is easy for us to update content. You use the content from www.velmarketa.com as an example. I will also post update logo and artwork. I also need a contact form with some type of validation or captcha.

Please omit Address maps

Target Market(s)

small business, service oriented companies. We provide IT Consulting, support and mangement

Industry/Entity Type

Information Technology

Coding

Coded - Design and coding required

Number of Pages Required

1 page

Font styles to use
Serif
Sans Serif

Requirements
Must have
• Contain logo attached, and content from existing web site www.velmarketa.com.
• Also need to update content easily, and be movable to different platforms.
• There is a catch phrase
• "Let us worry about your technology…” “ so you don’t have to!”
• Should be included.
Nice to have
• Testimonial page, Project page where we can post new and past projects and pictures
Should not have
• none

```html
<!DOCTYPE html>
<html lang="en">
<head>
<meta charset="utf-8">
<title>Velmarketa — IT Solutions</title>
<link href="https://fonts.googleapis.com/css2?family=Oswald:wght@500;600&family=Roboto:wght@400;500;700&display=swap" rel="stylesheet">
<style>
:root{
  --blue:#1e9ee0;
  --blue-dark:#0b6fae;
  --ink:#1a1a1a;
  --text:#555;
  --muted:#8a8a8a;
  --line:#222;
  --light:#f0f0f0;
  --white:#fff;
  --night:#0c0c0c;
  --hero-a:#03223a;
  --hero-b:#0b5f86;
}
*{box-sizing:border-box;margin:0;padding:0}
html,body{width:1200px;height:2990px;overflow:hidden}
body{position:relative;font-family:"Roboto",Arial,sans-serif;color:var(--text);background:var(--white)}
.abs{position:absolute}

/* header */
.site-header{left:0;top:0;width:1200px;height:110px;z-index:3;background:linear-gradient(180deg,rgba(2,18,32,.85),rgba(2,18,32,.35))}
.brand{left:40px;top:14px;display:flex;align-items:center;gap:12px}
.brand-mark{width:46px;height:46px;background:var(--blue)}
.brand-name{font:700 34px/1 "Roboto",sans-serif;color:var(--white);letter-spacing:1px}
.brand-tag{left:98px;top:64px;font-size:10px;color:#9cc9e6}
.top-contact{right:40px;top:22px;display:flex;gap:30px;font-size:15px;color:#cfe4f2}
.top-contact span{display:flex;align-items:center;gap:8px}
.main-nav{left:458px;top:56px;display:flex;height:54px}
.main-nav a{display:flex;align-items:center;padding:0 20px;font-size:18px;color:#e5eef5;text-decoration:none}
.main-nav a.active{background:var(--blue);color:var(--white);border-radius:4px 4px 0 0}

/* hero */
.hero{left:0;top:0;width:1200px;height:688px;background:radial-gradient(circle at 42% 62%,#2b8fc0 0,#0d4f78 22%,transparent 42%),radial-gradient(circle at 82% 45%,#c9d4de 0,#7b93a6 18%,transparent 38%),linear-gradient(120deg,var(--hero-a),var(--hero-b) 60%,#0a3a5c)}
.hero-title{left:46px;top:240px;font:600 40px/1 "Oswald",sans-serif;color:var(--white);z-index:2}
.hero-text{left:46px;top:294px;width:700px;font-size:18px;line-height:30px;color:#e7f1f8;z-index:2}
.btn{display:inline-block;background:var(--blue);color:var(--white);border-radius:5px;text-decoration:none}
.hero-btn{left:44px;top:398px;width:120px;height:42px;line-height:42px;text-align:center;font-size:17px;z-index:2}
.slider-dots{left:532px;top:640px;display:flex;gap:12px;z-index:2}
.slider-dots i{width:14px;height:14px;border:2px solid #cfe4f2;border-radius:50%}
.slider-dots i.on{background:var(--blue);border-color:var(--blue)}

/* section headings */
.sec-title{left:0;width:1200px;text-align:center;font:700 32px/1 "Roboto",sans-serif;color:var(--ink)}
.divider{width:210px;height:2px;background:var(--line)}
.divider::after{content:"";position:absolute;left:98px;top:-6px;width:14px;height:14px;background:var(--line)}
.divider.light{background:var(--white)}
.divider.light::after{background:var(--white)}

/* services */
.service-card{top:853px;height:192px;border:2px solid #3a3a3a;border-radius:8px;background:var(--white)}
.service-card.featured{border-color:var(--blue)}
.service-card p{position:absolute;left:20px;right:16px;top:84px;font-size:14px;line-height:24px;color:#444}
.service-icon{width:118px;height:118px;top:803px;background:#3a3a3a;border-radius:10px;display:flex;align-items:center;justify-content:center}
.service-icon.featured{background:var(--blue)}
.service-name{top:860px;font:500 17px/20px "Roboto",sans-serif;color:var(--ink)}

/* support */
.support-photo{left:0;top:1090px;width:540px;height:517px;background:linear-gradient(120deg,#8fb9d6,#d9e6ee 55%,#f4f6f8)}
.support-panel{left:528px;top:1090px;width:672px;height:517px;background:var(--light)}
.support-item{display:flex;gap:18px;width:300px}
.support-icon{flex:none;width:68px;height:68px;border:3px solid #333;border-radius:50%;display:flex;align-items:center;justify-content:center;background:var(--white)}
.support-icon.on{background:var(--blue);border-color:var(--blue)}
.support-item h3{font:500 18px/22px "Roboto",sans-serif;color:#333}
.support-item h3.on{color:var(--blue)}
.support-item p{font-size:13.5px;line-height:18px;color:#666;width:205px}

/* about */
.about-text{left:46px;top:1732px;width:690px;font-size:14.5px;line-height:27px;color:#555}
.about-text p+p{margin-top:10px}
.about-text b{color:var(--ink)}
.about-btn{left:44px;top:2006px;width:104px;height:36px;line-height:36px;text-align:center;font-size:15px}
.about-photo{left:690px;top:1650px;width:510px;height:350px;background:radial-gradient(ellipse at 55% 50%,#b9bfc6 0,#dfe2e6 40%,#fff 75%)}

/* testimonials */
.testimonials{left:0;top:2079px;width:1200px;height:458px;background:radial-gradient(circle at 80% 30%,#2a2a2a,transparent 40%),radial-gradient(circle at 20% 70%,#222,transparent 40%),var(--night)}
.quote-mark{left:0;width:1200px;text-align:center;font:700 60px/1 Georgia,serif;color:#ddd}
.quote-text{left:100px;top:2280px;width:1000px;text-align:center;font-size:17px;line-height:28px;color:#c9c9c9}
.quote-author{left:0;top:2426px;width:1200px;text-align:center;font:700 18px/1 "Roboto",sans-serif;color:var(--white)}
.quote-dots{left:564px;top:2476px;display:flex;gap:8px}
.quote-dots i{width:10px;height:10px;border:2px solid var(--blue);transform:rotate(45deg)}

/* contact */
.field{border:1px solid #bbb;border-radius:3px;background:var(--white);font-size:14px;color:#555;padding:0 14px;display:flex;align-items:center}
.field.area{align-items:flex-start;padding-top:14px}
.submit{left:967px;top:2671px;width:104px;height:107px;background:linear-gradient(180deg,#36b4ef,#1788c9);border-radius:3px;color:var(--white);font:700 19px/107px "Roboto",sans-serif;text-align:center}

/* footer */
.site-footer{left:0;top:2806px;width:1200px;height:184px;background:#050505}
.social{left:488px;top:2854px;display:flex;gap:9px}
.social i{width:28px;height:28px;background:#4a4a4a;border-radius:3px}
.social i:first-child{background:var(--blue)}
.footer-links{left:0;top:2900px;width:1200px;text-align:center;font-size:14px;color:#bbb}
.footer-links b{color:var(--white);font-weight:500}
.copyright{left:0;top:2928px;width:1200px;text-align:center;font-size:14px;color:#bbb}
</style>
</head>
<body>

<!-- hero -->
<div class="abs hero" role="img" aria-label="Digital technology backdrop with a glowing globe and a woman touching a virtual screen"></div>

<header class="abs site-header">
  <div class="abs brand"><span class="brand-mark"></span><span class="brand-name">VELMARKETA</span></div>
  <div class="abs brand-tag">Let us worry about your technology… so you don’t have to!</div>
  <div class="abs top-contact">
    <span><svg width="16" height="12" viewBox="0 0 16 12"><rect x="1" y="1" width="14" height="10" fill="none" stroke="#1e9ee0" stroke-width="1.6"/><path d="M1 1l7 6 7-6" fill="none" stroke="#1e9ee0" stroke-width="1.6"/></svg>info@velmarketa.com</span>
    <span><svg width="14" height="14" viewBox="0 0 14 14"><path d="M3 1l3 3-2 2c1 2 2 3 4 4l2-2 3 3-2 2C6 13 1 8 1 3z" fill="#1e9ee0"/></svg>+1 713.555.0148</span>
  </div>
  <nav class="abs main-nav">
    <a class="active">Home</a><a>About</a><a>Supports</a><a>Clients</a><a>Projects</a><a>Careers</a><a>Contact</a>
  </nav>
</header>

<h1 class="abs hero-title">IT SOLUTIONS THAT WORK FOR YOUR BUSINESS</h1>
<p class="abs hero-text">VMK is a technology solution provider based in Houston, Texas. Our goal is to make technology a non-issue for individuals and small to medium size businesses ranging from 5 to 150 Users. VMK has the experience, the tools, high-level technology</p>
<a class="abs btn hero-btn">Read More</a>
<div class="abs slider-dots"><i class="on"></i><i></i><i></i><i></i><i></i></div>

<!-- what we do -->
<h2 class="abs sec-title" style="top:732px">WHAT WE  DO</h2>
<div class="abs divider" style="left:495px;top:782px"></div>

<div class="abs service-card featured" style="left:76px;width:238px"><p>Our staff will design, service, administer and maintain your IT needs. We are well versed on all major operating…</p></div>
<div class="abs service-icon featured" style="left:44px">
  <svg width="64" height="64" viewBox="0 0 64 64" fill="none" stroke="#fff" stroke-width="4"><circle cx="26" cy="28" r="10"/><circle cx="46" cy="44" r="7"/><path d="M26 12v6M26 38v6M10 28h6M36 28h6M46 32v4M46 52v4M34 44h4M54 44h4"/></svg>
</div>
<div class="abs service-name" style="left:180px">Managed IT<br>Solutions</div>

<div class="abs service-card" style="left:373px;width:212px"><p>Do you need a quick solution to a technical problem? With our live remote -assistance tool…</p></div>
<div class="abs service-icon" style="left:340px">
  <svg width="64" height="64" viewBox="0 0 64 64" fill="none" stroke="#fff" stroke-width="4"><circle cx="32" cy="18" r="8"/><rect x="12" y="32" width="40" height="24" rx="2"/></svg>
</div>
<div class="abs service-name" style="left:486px;top:862px">Remote<br>Diagnostic<br>&amp; Support</div>

<div class="abs service-card" style="left:644px;width:208px"><p>Lorem ipsum dolor sitet, consectetur adipiscingilt. Quisque pulvinar pretium interdumuisque coallis…</p></div>
<div class="abs service-icon" style="left:610px">
  <svg width="64" height="64" viewBox="0 0 64 64" fill="none" stroke="#fff" stroke-width="4"><rect x="14" y="8" width="36" height="14"/><rect x="10" y="30" width="44" height="24" rx="2"/><path d="M20 15h4"/></svg>
</div>
<div class="abs service-name" style="left:748px;top:862px">Hosting<br>and<br>Virtulization</div>

<div class="abs service-card" style="left:915px;width:240px"><p>Do you need a quick solution to a technical problem? With our live remote-assistanc tool, a member of our support…</p></div>
<div class="abs service-icon" style="left:880px">
  <svg width="64" height="64" viewBox="0 0 64 64" fill="none" stroke="#fff" stroke-width="4"><rect x="10" y="20" width="44" height="32" rx="2"/><path d="M22 44l20-20M40 22l4 4"/></svg>
</div>
<div class="abs service-name" style="left:1020px;top:862px">IT<br>Infrastructure<br>Design &amp;<br>Installation</div>

<!-- support -->
<div class="abs support-photo" role="img" aria-label="Photo of two young colleagues working together at a laptop in a bright office"></div>
<div class="abs support-panel"></div>
<h2 class="abs sec-title" style="left:528px;width:560px;top:1134px">IT SUPPORT SOLUTIONS</h2>
<div class="abs divider" style="left:704px;top:1186px"></div>

<div class="abs support-item" style="left:546px;top:1216px"><div class="support-icon on"><svg width="32" height="32" viewBox="0 0 32 32" fill="#fff"><circle cx="16" cy="16" r="4"/><circle cx="6" cy="8" r="3"/><circle cx="26" cy="8" r="3"/><circle cx="16" cy="28" r="3"/><path d="M6 8l10 8 10-8M16 16v12" stroke="#fff" stroke-width="2"/></svg></div><div><h3 class="on">Network Adminstration</h3><p>risus nec commodo porttitor, arcu ipsum imperdiet lacus,</p></div></div>
<div class="abs support-item" style="left:892px;top:1216px"><div class="support-icon"><svg width="30" height="30" viewBox="0 0 30 30" fill="none" stroke="#333" stroke-width="2.5"><rect x="4" y="6" width="18" height="14"/><rect x="24" y="6" width="4" height="18"/><path d="M10 24h8"/></svg></div><div><h3>Desktop Support</h3><p>Praesent consecteturant siut neque luctusnec luc</p></div></div>

<div class="abs support-item" style="left:546px;top:1309px"><div class="support-icon"><svg width="30" height="30" viewBox="0 0 30 30" fill="none" stroke="#333" stroke-width="2.5"><rect x="8" y="4" width="6" height="10"/><rect x="16" y="4" width="6" height="10"/><path d="M11 14v12M19 14v12"/></svg></div><div><h3>Netwrok Cabling</h3><p>Asrit consectetur tellus nunc vitae lacusliquam phare</p></div></div>
<div class="abs support-item" style="left:892px;top:1309px"><div class="support-icon"><svg width="30" height="30" viewBox="0 0 30 30" fill="none" stroke="#333" stroke-width="2.5"><path d="M3 12a17 17 0 0 1 24 0M7 16a11 11 0 0 1 16 0M11 20a5 5 0 0 1 8 0"/><circle cx="15" cy="24" r="1.5" fill="#333"/></svg></div><div><h3>Wireless Network</h3><p>Tus massa pulvinaraece nasnisl neque elementu</p></div></div>

<div class="abs support-item" style="left:546px;top:1399px"><div class="support-icon"><svg width="30" height="30" viewBox="0 0 30 30" fill="none" stroke="#333" stroke-width="2.5"><rect x="4" y="10" width="22" height="14"/><path d="M8 10V6h4v4"/><path d="M16 14h6M16 18h6"/></svg></div><div><h3>Telecommunications</h3><p>tra nisi enim, vitae interdum nisl euismod euusce utneque</p></div></div>
<div class="abs support-item" style="left:892px;top:1399px"><div class="support-icon"><svg width="30" height="30" viewBox="0 0 30 30" fill="none" stroke="#333" stroke-width="2.5"><path d="M15 3l10 4v8c0 6-5 10-10 12C10 25 5 21 5 15V7z"/></svg></div><div><h3>Antivirus Soultions</h3><p>Smet massa euursus vrr ipsum Vivamus vehicula</p></div></div>

<div class="abs support-item" style="left:546px;top:1489px"><div class="support-icon"><svg width="30" height="30" viewBox="0 0 30 30" fill="none" stroke="#333" stroke-width="2.5"><circle cx="15" cy="15" r="11"/><circle cx="15" cy="15" r="5"/></svg></div><div><h3>Disaster Recovery</h3><p>ipsum. Vestibulum a augue nisi. Nulla luctus leo mi,</p></div></div>
<div class="abs support-item" style="left:892px;top:1489px"><div class="support-icon"><svg width="30" height="30" viewBox="0 0 30 30" fill="none" stroke="#333" stroke-width="2.5"><rect x="4" y="6" width="22" height="15"/><path d="M10 26h10M15 21v5"/></svg></div><div><h3>Web Design</h3><p>Bibendum augue ac laci sagittis accums pulvinar</p></div></div>

<!-- about -->
<div class="abs about-photo" role="img" aria-label="Photo of a businesswoman holding a cup while working at a laptop"></div>
<h2 class="abs sec-title" style="left:0;width:1176px;top:1652px">ABOUT US</h2>
<div class="abs divider" style="left:483px;top:1704px"></div>
<div class="abs about-text">
  <p><b>Outsourcing</b> is subcontracting a process, such as product design or manufacturing, to a third-party company. The decision to outsource is often made in the interest of lowering firm costs, redirecting or conserving energy directed at the competencies of a particular business, or to make more efficient use of land, labor, capital, (information) technology and resources.   Outsourcing became part of the business lexicon during the 1980s.</p>
  <p>VMK is a technology solution provider based in Houston, Texas. Our goal is to make technology a non-issue for individuals and small to medium size businesses ranging from 5 to 150 Users. VMK has the experience, the tools, high-level technology solutions and training to power your business and your work force. We understand that all business's have one goal in common!</p>
</div>
<a class="abs btn about-btn">Read More</a>

<!-- testimonials -->
<section class="abs testimonials" role="img" aria-label="Dark backdrop of faint office photos"></section>
<h2 class="abs sec-title" style="top:2130px;color:#fff">TESTIMONIALS</h2>
<div class="abs divider light" style="left:495px;top:2178px"></div>
<div class="abs quote-mark" style="top:2224px">“</div>
<p class="abs quote-text">We are extremely happy with our frank, open, and honest relationship with Northgate Partners. Northgate Partners’ solution and delivery capabilities in the technology business not only improved the time to market and predictability, but reduced the cost of implementation</p>
<div class="abs quote-mark" style="top:2362px;font-size:44px;color:#aaa">”</div>
<div class="abs quote-author">Lorem ipsum | Company Name</div>
<div class="abs quote-dots"><i style="background:var(--blue)"></i><i></i><i></i><i></i></div>

<!-- contact -->
<h2 class="abs sec-title" style="top:2584px">CONTACT US</h2>
<div class="abs divider" style="left:495px;top:2634px"></div>
<form>
  <div class="abs field" style="left:126px;top:2671px;width:254px;height:44px">First Name:</div>
  <div class="abs field" style="left:399px;top:2671px;width:256px;height:44px">Last Name:</div>
  <div class="abs field" style="left:126px;top:2735px;width:254px;height:44px">Phone:</div>
  <div class="abs field" style="left:399px;top:2735px;width:256px;height:44px">Email:</div>
  <div class="abs field area" style="left:674px;top:2671px;width:274px;height:108px">Comments:</div>
  <div class="abs submit">SUBMIT</div>
</form>

<!-- footer -->
<footer class="abs site-footer"></footer>
<div class="abs social"><i></i><i></i><i></i><i></i><i></i><i></i></div>
<div class="abs footer-links"><b>Home</b>   /  About Us   /  Supports   /  Client   /  Careers   /  Contact</div>
<div class="abs copyright">© 2017. velmarketa.All Rights Reserved.</div>

</body>
</html>
```